Real Estate Marketing Flyer (To Be Mailed)

Design a Flyer To be Mailed to Potential Home Sellers.
Possible Texts to Use:
*Lehighton Home Owners: Opportunity is Knocking in 2020!
*Industry is moving in
*Housing Inventory is Critically Low
*Entry Level Homes in High Demand
*Qualified Buyers are searching Now
*Interest Rates Projected to Rise by year end
*Now is the Time to Sell
*Trust My Proven Track Record to get the job done well
-----------------------------------------------
My Info for the Piece:
Orsolya Markey
Ke/Tor Boundless
2417 Pellum Ave
Whitehall Pa 18099
484 555 0173
610 555 0142
Updates
Please use Ke/Tor Colors of Blue and Red if Possible. Also, I will upload my headshot to use.

```html
<!DOCTYPE html>
<html lang="en">
<head>
<meta charset="utf-8">
<title>Lehighton Home Owners – Seller Flyer</title>
<link rel="stylesheet" href="https://fonts.googleapis.com/css2?family=Raleway:wght@300;400;600;700&family=Quicksand:wght@400;500&family=Lato:wght@700&display=swap">
<style>
  :root {
    --stage: #dcdbda;
    --paper: #f6f6f5;
    --brand-red: #e5353a;
    --brand-red-soft: rgba(229, 53, 58, 0.9);
    --ink: #545454;
    --ink-dark: #3f3f3f;
    --band: #4b4849;
    --band-deep: #5a5758;
    --muted: #c9c7c7;
    --white: #ffffff;
  }
  * { box-sizing: border-box; margin: 0; padding: 0; }
  html, body { width: 1200px; height: 800px; overflow: hidden; }
  body { background: var(--stage); position: relative; }

  .flyer {
    position: absolute;
    left: 332px;
    top: 20px;
    width: 860px;
    height: 1220px;
    transform: scale(0.6233);
    transform-origin: top left;
    background: var(--paper);
    box-shadow: 0 30px 50px rgba(0,0,0,0.18);
    overflow: hidden;
  }
  .flyer-art { position: absolute; inset: 0; width: 860px; height: 1220px; }

  .headline {
    position: absolute; left: 28px; top: 300px;
    color: var(--white); font-family: "Raleway", sans-serif;
  }
  .headline-audience { font-weight: 300; font-size: 35px; line-height: 1; }
  .headline-key { font-weight: 700; font-size: 56px; line-height: 1; margin-top: 14px; letter-spacing: 0.3px; }
  .headline-rest { font-weight: 300; font-size: 62px; line-height: 1; margin-top: 4px; }

  .market-points {
    position: absolute; right: 40px; top: 580px; list-style: none;
    font-family: "Raleway", sans-serif; font-size: 21px; color: var(--ink);
    text-align: right;
  }
  .market-points li { height: 44px; line-height: 38px; }
  .market-points li::after {
    content: ""; display: inline-block; width: 13px; height: 13px;
    border-radius: 50%; background: var(--brand-red); margin-left: 16px;
    vertical-align: 1px;
  }

  .call-to-action {
    position: absolute; left: 514px; top: 806px; width: 346px; height: 42px;
    border-radius: 21px 0 0 21px; background: var(--brand-red);
    color: var(--white); font-family: "Raleway", sans-serif; font-weight: 700;
    font-size: 22px; line-height: 42px; padding-left: 21px;
  }

  .agent-photo {
    position: absolute; left: 70px; top: 739px; width: 278px; height: 336px;
    border-radius: 40px;
    background: radial-gradient(circle at 50% 40%, #6b4a3e 0%, #3a2b28 55%, #1e1a1a 100%);
  }

  .agent-promise {
    position: absolute; left: 83px; top: 1088px;
    color: var(--white); font-family: "Quicksand", sans-serif; font-size: 19px; line-height: 27px;
  }

  .agent-card {
    position: absolute; right: 42px; top: 964px; text-align: right;
  }
  .agent-name {
    font-family: "Raleway", sans-serif; font-weight: 600; font-size: 37px;
    color: var(--brand-red); line-height: 1;
  }
  .agent-office {
    font-family: "Raleway", sans-serif; font-size: 22px; color: var(--ink-dark); margin-top: 4px;
  }
  .agent-phones, .agent-address {
    font-family: "Lato", sans-serif; font-weight: 700; font-size: 16.5px; color: var(--ink-dark);
  }
  .agent-phones { margin-top: 32px; }
  .agent-address { margin-top: 10px; }
  .phone { margin-left: 12px; white-space: nowrap; }
  .phone svg { width: 20px; height: 16px; vertical-align: -2px; margin-right: 4px; }

  .disclaimer {
    position: absolute; left: 0; right: 0; top: 1156px; text-align: center;
    font-family: "Raleway", sans-serif; font-size: 16.5px; line-height: 26px; color: var(--muted);
  }
</style>
</head>
<body>
  <article class="flyer">
    <svg class="flyer-art" viewBox="0 0 860 1220">
      <defs>
        <linearGradient id="homePhotoTone" x1="0" y1="0" x2="0" y2="1">
          <stop offset="0" stop-color="#6f8fb8"/>
          <stop offset="0.35" stop-color="#b9c8d8"/>
          <stop offset="0.55" stop-color="#8a6b55"/>
          <stop offset="0.75" stop-color="#55613f"/>
          <stop offset="1" stop-color="#a58f6f"/>
        </linearGradient>
        <linearGradient id="bandTone" x1="0" y1="0" x2="0" y2="1">
          <stop offset="0" stop-color="var(--band-deep)"/>
          <stop offset="1" stop-color="var(--band)"/>
        </linearGradient>
        <clipPath id="heroClip"><rect x="0" y="0" width="860" height="692"/></clipPath>
      </defs>

      <rect class="home-photo" x="0" y="0" width="860" height="700" fill="url(#homePhotoTone)"
            role="img" aria-label="Photo of a brick and stone two-storey house under a blue sky"/>

      <g clip-path="url(#heroClip)">
        <rect class="headline-diamond" x="-80" y="120" width="540" height="540" rx="90"
              fill="var(--brand-red-soft)" transform="rotate(45 190 390)"/>
      </g>

      <path class="content-panel" fill="var(--paper)"
            d="M0 692 H360 Q392 692 412 664 L468 556 Q482 528 512 528 H860 V1220 H0 Z"/>

      <path class="footer-band" fill="url(#bandTone)"
            d="M0 1012 H410 Q432 1012 448 1032 L508 1108 Q526 1132 556 1132 H860 V1220 H0 Z"/>
    </svg>

    <div class="headline">
      <p class="headline-audience">Lehighton Home Owners</p>
      <p class="headline-key">OPPORTUNITY</p>
      <p class="headline-rest">is Knocking<br>in 2020</p>
    </div>

    <ul class="market-points">
      <li>Industry is moving in</li>
      <li>Housing Inventory is Critically Low</li>
      <li>Entry Level Homes in High Demand</li>
      <li>Qualified Buyers are searching Now</li>
      <li>Interest rates projected to rise by year end</li>
    </ul>

    <p class="call-to-action">NOW IS THE TIME TO SELL</p>

    <div class="agent-photo" role="img" aria-label="Headshot of the agent, Orsolya Markey"></div>

    <p class="agent-promise">Trust My Proven Track<br>Record to get the job done well</p>

    <div class="agent-card">
      <p class="agent-name">ORSOLYA MARKEY</p>
      <p class="agent-office">Harrow Lane Real Estate</p>
      <p class="agent-phones">
        <span class="phone"><svg viewBox="0 0 20 16"><path fill="var(--brand-red)" d="M2 5 Q10 0 18 5 L16 8 L13 6.5 V5 Q10 4 7 5 V6.5 L4 8 Z M5 9 H15 L17 15 H3 Z"/></svg>484.555.0173</span>
        <span class="phone"><svg viewBox="0 0 20 16"><path fill="var(--brand-red)" d="M2 5 Q10 0 18 5 L16 8 L13 6.5 V5 Q10 4 7 5 V6.5 L4 8 Z M5 9 H15 L17 15 H3 Z"/></svg>610.555.0142</span>
      </p>
      <p class="agent-address">2417 Pellum Ave, Whitehall Pa 18099</p>
    </div>

    <p class="disclaimer">"All information deed reliable but not guaranteed. Not meant as a solicitation<br>of your listing. Each office independently owned and operated."</p>
  </article>
</body>
</html>
```